FinTech company looking to revamp and expand client-facing interface for our financial models

Halvern Ledgerworks currently has a very simple website that allows clients to interact with our financial models. We are looking to completely redesign the current site and add several extra pages to provide extra functionality. We want the design to have a modern, slick feel, that will work on both a desktop or a tablet. It should be straightforward for clients to move between different pages at any time, and clear from the layout how to interact with the more advanced features. We have included screenshots of existing pages in the attached design brief, as well as sketches of the functionality required by the new pages, but can't provide a direct link to the current site.
Target Market(s)
Professional investors that will be paying to access the interface
Industry/Entity Type
Finance
Number of Pages Required
4 page
Colors
Designer to choose colors to be used in the design.
Look and feel
Each slider illustrates characteristics of the customer's brand and the style your logo design should communicate.

```html
<!DOCTYPE html>
<html lang="en">
<head>
<meta charset="utf-8">
<title>HLX – Models</title>
<link href="https://fonts.googleapis.com/css2?family=Roboto:wght@300;400;500;700&display=swap" rel="stylesheet">
<style>
:root{
  --stage:#676767;
  --nav:#222222;
  --white:#ffffff;
  --ink:#222222;
  --muted:#9aa0a6;
  --link:#1a9fe0;
  --neg:#e8201f;
  --head:#e7eaed;
  --line:#e6e6e6;
  --star:#f5a623;
  --export:#1ea7e8;
  --filter:#1f4f7a;
  --filter-on:#8fa5b9;
  --panel:#eef2f5;
  --field:#dde5eb;
  --panel-ink:#2a5580;
}
*{box-sizing:border-box;margin:0;padding:0}
html,body{width:1200px;height:2261px;overflow:hidden;background:var(--stage)}
body{font-family:"Roboto",Arial,sans-serif;color:var(--ink)}
.board{position:relative;width:1366px;height:2576px;transform:scale(0.87848);transform-origin:0 0;background:var(--stage)}
.screen{position:absolute;left:0;width:1366px;background:var(--white);overflow:hidden}
.screen--preview{left:268px;top:191px;height:850px;transform:scale(0.6083);transform-origin:0 0}
.screen--table{top:938px;height:768px}
.screen--filters{top:1806px;height:770px}

.topbar{position:absolute;left:0;top:0;width:100%;height:56px;background:var(--nav);color:var(--white)}
.brand{position:absolute;left:32px;top:18px;font-size:19px;font-weight:400;letter-spacing:.5px}
.nav-item{position:absolute;top:20px;display:flex;align-items:center;gap:8px;font-size:11.5px;font-weight:700;text-transform:uppercase;letter-spacing:.2px}
.nav-item svg{width:15px;height:15px;fill:var(--white)}
.nav-item.is-active::after{content:"";position:absolute;left:-16px;right:-16px;top:36px;height:3px;background:#555}
.user{position:absolute;right:32px;top:21px;font-size:11px;display:flex;gap:8px;align-items:center}
.user svg{width:10px;height:10px;stroke:var(--white);fill:none;stroke-width:1.6}

.page-head{position:absolute;left:0;top:56px;width:100%;height:104px}
.page-title{position:absolute;left:33px;top:48px;font-size:33px;font-weight:300;letter-spacing:1px}
.select{position:absolute;top:52px;height:30px;border-bottom:1px solid #333;font-size:17px;font-weight:300;padding:2px 8px;display:flex;justify-content:space-between;align-items:center}
.select svg{width:12px;height:12px;stroke:#333;fill:none;stroke-width:1.5}
.btn{position:absolute;top:48px;width:96px;height:32px;border-radius:2px;color:var(--white);font-size:11.5px;font-weight:700;display:flex;align-items:center;justify-content:center;gap:8px}
.btn svg{width:14px;height:14px}
.btn--export{background:var(--export)}
.btn--filter{background:var(--filter)}
.btn--filter.is-on{background:var(--filter-on)}

.models{position:absolute;left:0;top:160px;border-collapse:collapse;table-layout:fixed;width:1366px}
.models th{height:40px;background:var(--head);font-size:11px;font-weight:700;text-align:left;padding-left:16px;border-left:1px solid #d8dcdf;white-space:nowrap;overflow:hidden}
.models th .caret{color:var(--muted);font-size:8px;margin-left:4px}
.models th.id .caret{color:var(--link)}
.models td{height:57px;font-size:11.5px;padding-left:16px;border-left:1px solid var(--line);border-bottom:1px solid var(--line);line-height:14px;white-space:nowrap;overflow:hidden}
.models td.fav{padding-left:12px;font-size:16px;color:#c6c6c6}
.models td.fav.on{color:var(--star)}
.models td.id{color:var(--link);font-weight:500}
.models .neg{color:var(--neg)}
.models th:first-child,.models td:first-child{border-left:none}

.pager{position:absolute;top:170px;display:flex;gap:6px}
.pager span{width:22px;height:22px;border-radius:50%;display:flex;align-items:center;justify-content:center}
.pager svg{width:12px;height:12px;stroke:var(--white);fill:none;stroke-width:2}
.pager .prev{background:#8a8a8a}
.pager .next{background:#111}

.menu{position:absolute;left:368px;top:56px;width:152px;background:var(--white);box-shadow:0 3px 10px rgba(0,0,0,.18);padding:4px 16px}
.menu li{list-style:none;height:41px;line-height:41px;padding-left:16px;font-size:11px;font-weight:700;border-bottom:1px solid var(--line)}
.menu li:last-child{border-bottom:none}

.filters{position:absolute;right:0;top:56px;width:256px;bottom:0;background:var(--panel);padding:0 32px}
.filters .close{position:absolute;right:8px;top:10px;width:14px;height:14px;stroke:#8a9aa8;stroke-width:1.3}
.filters h2{margin-top:28px;font-size:19px;font-weight:400;color:var(--panel-ink);letter-spacing:.5px}
.filters label{display:block;font-size:9px;font-weight:700;color:var(--panel-ink);margin-top:22px;margin-bottom:6px}
.filters h2+label{margin-top:16px}
.field{height:30px;background:var(--field);display:flex;justify-content:flex-end;align-items:center;padding:0 12px;font-size:11px;color:var(--ink)}
.field svg{width:11px;height:11px}
.pair{display:flex;gap:6px}
.pair .field:first-child{width:92px;justify-content:space-between}
.pair .field:last-child{flex:1;justify-content:flex-start}
.filters .pair+label,.filters .field+label{margin-top:28px}
.actions{display:flex;gap:4px;margin-top:28px}
.actions span{width:94px;height:40px;display:flex;align-items:center;justify-content:center;font-size:11.5px;font-weight:700;border-radius:2px}
.reset{border:1px solid var(--filter);color:var(--filter)}
.apply{background:var(--filter);color:var(--white)}
.scroll{position:absolute;right:10px;top:70px;width:4px;height:70px;background:#cfd7de;border-radius:2px}
</style>
</head>
<body>
<div class="board">

<!-- ===== Preview: models with filters open ===== -->
<section class="screen screen--preview">
  <header class="topbar">
    <div class="brand">HLX</div>
    <div class="nav-item" style="left:384px"><svg viewBox="0 0 16 16"><path d="M8 5a3 3 0 1 0 0 6 3 3 0 0 0 0-6zm6.5 4-.1-2 1.6-1.3-1.5-2.6-2 .7-1.7-1L10.5 1h-3l-.4 2-1.7 1-2-.8L1.9 5.8 3.5 7l-.1 2-1.6 1.2 1.5 2.6 2-.7 1.7 1 .4 2h3l.4-2 1.7-1 2 .7 1.5-2.6z"/></svg>Models</div>
    <div class="nav-item" style="left:496px"><svg viewBox="0 0 16 16"><path d="M8 1l2.2 4.6 5 .6-3.7 3.4 1 5L8 12.2 3.5 14.6l1-5L.8 6.2l5-.6z"/></svg>Favourites</div>
    <div class="nav-item" style="left:630px"><svg viewBox="0 0 16 16"><path d="M1 5h11l-3-3h2l4 4-4 4H9l3-3H1zm14 6H4l3 3H5l-4-4 4-4h2L4 9h11z"/></svg>Sensitivities</div>
    <div class="nav-item" style="left:775px"><svg viewBox="0 0 16 16"><circle cx="8" cy="4.5" r="3.5"/><path d="M1 16c0-4 3-7 7-7s7 3 7 7z"/></svg>Portfolio</div>
    <div class="nav-item" style="left:901px"><svg viewBox="0 0 16 16"><path d="M10 0 3 9h4l-2 7 8-10H9z"/></svg>Backtest</div>
    <div class="user">Username <svg viewBox="0 0 10 10"><path d="M1 3l4 4 4-4"/></svg></div>
  </header>
  <div class="page-head">
    <h1 class="page-title">MODELS</h1>
    <div class="select" style="left:190px;width:146px">Equities<svg viewBox="0 0 12 12"><path d="M1 4l5 5 5-5"/></svg></div>
    <div class="select" style="left:350px;width:96px">250D<svg viewBox="0 0 12 12"><path d="M1 4l5 5 5-5"/></svg></div>
    <div class="btn btn--export" style="left:830px"><svg viewBox="0 0 14 14" fill="none" stroke="#fff" stroke-width="1.5"><path d="M6 2H1v11h11V8M8 1h5v5M13 1 6 8"/></svg>EXPORT</div>
    <div class="btn btn--filter is-on" style="left:930px"><svg viewBox="0 0 14 14" fill="#fff"><path d="M0 1h14L9 7v6L5 11V7z"/></svg>FILTER</div>
  </div>
  <table class="models">
    <colgroup><col style="width:40px"><col style="width:90px"><col style="width:137px"><col style="width:105px"><col style="width:97px"><col style="width:97px"><col style="width:97px"><col style="width:97px"><col style="width:97px"><col style="width:97px"><col style="width:97px"><col style="width:105px"><col style="width:105px"><col style="width:105px"></colgroup>
    <thead><tr><th></th><th class="id">ID<span class="caret">▼</span></th><th>SECTOR<span class="caret">▼</span></th><th>TIME<span class="caret">▼</span></th><th>QUALITY<span class="caret">▼</span></th><th>STAT 1<span class="caret">▼</span></th><th>STAT 2<span class="caret">▼</span></th><th>STAT 3<span class="caret">▼</span></th><th>STAT 4<span class="caret">▼</span></th><th>STAT 5<span class="caret">▼</span></th><th>STAT 6<span class="caret">▼</span></th><th>STAT 7<span class="caret">▼</span></th><th>STAT 8<span class="caret">▼</span></th><th>STAT 9<span class="caret">▼</span></th></tr></thead>
    <tbody>
      <tr><td class="fav on">★</td><td class="id">Model 1</td><td>Materials</td><td>2019/07/03<br>12:15:00.000</td><td>30.2288</td><td>2.01574</td><td>22.305</td><td class="neg">-0.149368</td><td>22.3054</td><td>4.63714</td><td>0.945706</td><td>2.81949</td><td>2.60858</td><td>1.84256</td></tr>
      <tr><td class="fav">☆</td><td class="id">Model 2</td><td>Industrials</td><td>2019/07/03<br>12:15:00.000</td><td>32.8694</td><td>0.87307</td><td>32.185</td><td class="neg">-0.0336927</td><td>33.9911</td><td>11.5693</td><td class="neg">-0.472968</td><td class="neg">-0.830458</td><td>6.80646</td><td>0.39612</td></tr>
      <tr><td class="fav">☆</td><td class="id">Model 3</td><td>Consumer<br>Discretionary</td><td>2019/07/03<br>12:15:00.000</td><td>1.66002</td><td class="neg">-0.569222</td><td>159.814</td><td>0.0252328</td><td>172.616</td><td>10.2875</td><td class="neg">-0.750396</td><td class="neg">-0.385309</td><td>4.69146</td><td>1.31029</td></tr>
      <tr><td class="fav on">★</td><td class="id">Model 4</td><td>Information<br>Technology</td><td>2019/07/03<br>12:15:00.000</td><td>45.6856</td><td>0.412148</td><td>202.488</td><td>0.00849232</td><td>205.834</td><td>11.9094</td><td class="neg">-0.137913</td><td>0.449595</td><td>3.85106</td><td>0.02858</td></tr>
      <tr><td class="fav on">★</td><td class="id">Model 5</td><td>Information<br>Technology</td><td>2019/07/03<br>12:15:00.000</td><td>75.7733</td><td>7.06728</td><td>188.605</td><td>0.016913</td><td>181.665</td><td>3.82241</td><td>0.981019</td><td>1.29847</td><td>3.34927</td><td>1.88511</td></tr>
      <tr><td class="fav">☆</td><td class="id">Model 6</td><td>Industrials</td><td>2019/07/03<br>12:15:00.000</td><td>4.96502</td><td class="neg">-0.00369</td><td>48.923</td><td>0.179453</td><td>54.19</td><td>6.02448</td><td>0.183421</td><td>0.118642</td><td>6.80646</td><td>4.00219</td></tr>
      <tr><td class="fav">☆</td><td class="id">Model 7</td><td>Industrials</td><td>2019/07/03<br>12:15:00.000</td><td>22.94521</td><td>1.00634</td><td>82.735</td><td class="neg">-0.005328</td><td>62.4901</td><td>9.25216</td><td>0.037253</td><td>0.294521</td><td>4.69146</td><td>10.82611</td></tr>
      <tr><td class="fav">☆</td><td class="id">Model 8</td><td>Information<br>Technology</td><td>2019/07/03<br>12:15:00.000</td><td>2.48091</td><td>0.92301</td><td>98.3865</td><td>0.117436</td><td>66.004</td><td>7.82366</td><td>0.286345</td><td>0.3368901</td><td>3.85106</td><td>4.01112</td></tr>
      <tr><td class="fav">☆</td><td class="id">Model 9</td><td>Information<br>Technology</td><td>2019/07/03<br>12:15:00.000</td><td>29.0965</td><td>1.99652</td><td>54.9202</td><td>0.129685</td><td>49.002</td><td>5.92456</td><td>0.62961</td><td>1.1190652</td><td>3.34927</td><td>0.91734</td></tr>
      <tr><td class="fav">☆</td><td class="id">Model 10</td><td>Materials</td><td>2019/07/03<br>12:15:00.000</td><td>10.9523</td><td>3.95261</td><td>62.816</td><td>0.62341</td><td>91.8452</td><td>8.02261</td><td>0.3889</td><td>1.008442</td><td>6.80646</td><td>5.55299</td></tr>
    </tbody>
  </table>
  <div class="pager" style="left:1003px"><span class="prev"><svg viewBox="0 0 12 12"><path d="M10 6H2m3-3L2 6l3 3"/></svg></span><span class="next"><svg viewBox="0 0 12 12"><path d="M2 6h8M7 3l3 3-3 3"/></svg></span></div>
  <aside class="filters">
    <svg class="close" viewBox="0 0 14 14"><path d="M2 2l10 10M12 2 2 12"/></svg>
    <div class="scroll"></div>
    <h2>FILTERS</h2>
    <label>SECTORS</label><div class="field"><svg viewBox="0 0 12 12" fill="none" stroke="#2a5580" stroke-width="1.3"><path d="M2 4l4 4 4-4"/></svg></div>
    <label>TIME FROM</label><div class="field"><svg viewBox="0 0 12 12" fill="#2a5580"><path d="M1 3h10v8H1zm2-2h1v2H3zm5 0h1v2H8z"/></svg></div>
    <label>TIME TO</label><div class="field"><svg viewBox="0 0 12 12" fill="#2a5580"><path d="M1 3h10v8H1zm2-2h1v2H3zm5 0h1v2H8z"/></svg></div>
    <label>QUALITY</label><div class="pair"><div class="field"><span></span><svg viewBox="0 0 12 12" fill="none" stroke="#2a5580" stroke-width="1.3"><path d="M2 4l4 4 4-4"/></svg></div><div class="field"></div></div>
    <label>STAT 1</label><div class="pair"><div class="field"><span></span><svg viewBox="0 0 12 12" fill="none" stroke="#2a5580" stroke-width="1.3"><path d="M2 4l4 4 4-4"/></svg></div><div class="field"></div></div>
    <label>STAT 2</label><div class="pair"><div class="field"><span></span><svg viewBox="0 0 12 12" fill="none" stroke="#2a5580" stroke-width="1.3"><path d="M2 4l4 4 4-4"/></svg></div><div class="field"></div></div>
    <label>STAT 3</label><div class="pair"><div class="field"><span></span><svg viewBox="0 0 12 12" fill="none" stroke="#2a5580" stroke-width="1.3"><path d="M2 4l4 4 4-4"/></svg></div><div class="field"></div></div>
    <label>STAT 4</label><div class="pair"><div class="field"><span></span><svg viewBox="0 0 12 12" fill="none" stroke="#2a5580" stroke-width="1.3"><path d="M2 4l4 4 4-4"/></svg></div><div class="field"></div></div>
    <div class="actions"><span class="reset">RESET</span><span class="apply">APPLY</span></div>
  </aside>
</section>

<!-- ===== Models table ===== -->
<section class="screen screen--table">
  <header class="topbar">
    <div class="brand">HLX</div>
    <div class="nav-item" style="left:384px"><svg viewBox="0 0 16 16"><path d="M8 5a3 3 0 1 0 0 6 3 3 0 0 0 0-6zm6.5 4-.1-2 1.6-1.3-1.5-2.6-2 .7-1.7-1L10.5 1h-3l-.4 2-1.7 1-2-.8L1.9 5.8 3.5 7l-.1 2-1.6 1.2 1.5 2.6 2-.7 1.7 1 .4 2h3l.4-2 1.7-1 2 .7 1.5-2.6z"/></svg>Models</div>
    <div class="nav-item" style="left:496px"><svg viewBox="0 0 16 16"><path d="M8 1l2.2 4.6 5 .6-3.7 3.4 1 5L8 12.2 3.5 14.6l1-5L.8 6.2l5-.6z"/></svg>Favourites</div>
    <div class="nav-item" style="left:630px"><svg viewBox="0 0 16 16"><path d="M1 5h11l-3-3h2l4 4-4 4H9l3-3H1zm14 6H4l3 3H5l-4-4 4-4h2L4 9h11z"/></svg>Sensitivities</div>
    <div class="nav-item" style="left:775px"><svg viewBox="0 0 16 16"><circle cx="8" cy="4.5" r="3.5"/><path d="M1 16c0-4 3-7 7-7s7 3 7 7z"/></svg>Portfolio</div>
    <div class="nav-item" style="left:901px"><svg viewBox="0 0 16 16"><path d="M10 0 3 9h4l-2 7 8-10H9z"/></svg>Backtest</div>
    <div class="user">Username <svg viewBox="0 0 10 10"><path d="M1 3l4 4 4-4"/></svg></div>
  </header>
  <div class="page-head">
    <h1 class="page-title">MODELS</h1>
    <div class="select" style="left:190px;width:146px">Equities<svg viewBox="0 0 12 12"><path d="M1 4l5 5 5-5"/></svg></div>
    <div class="select" style="left:350px;width:96px">250D<svg viewBox="0 0 12 12"><path d="M1 4l5 5 5-5"/></svg></div>
    <div class="btn btn--export" style="left:1138px"><svg viewBox="0 0 14 14" fill="none" stroke="#fff" stroke-width="1.5"><path d="M6 2H1v11h11V8M8 1h5v5M13 1 6 8"/></svg>EXPORT</div>
    <div class="btn btn--filter" style="left:1238px"><svg viewBox="0 0 14 14" fill="#fff"><path d="M0 1h14L9 7v6L5 11V7z"/></svg>FILTER</div>
  </div>
  <table class="models">
    <colgroup><col style="width:40px"><col style="width:90px"><col style="width:137px"><col style="width:105px"><col style="width:97px"><col style="width:97px"><col style="width:97px"><col style="width:97px"><col style="width:97px"><col style="width:97px"><col style="width:97px"><col style="width:105px"><col style="width:105px"><col style="width:105px"></colgroup>
    <thead><tr><th></th><th class="id">ID<span class="caret">▼</span></th><th>SECTOR<span class="caret">▼</span></th><th>TIME<span class="caret">▼</span></th><th>QUALITY<span class="caret">▼</span></th><th>STAT 1<span class="caret">▼</span></th><th>STAT 2<span class="caret">▼</span></th><th>STAT 3<span class="caret">▼</span></th><th>STAT 4<span class="caret">▼</span></th><th>STAT 5<span class="caret">▼</span></th><th>STAT 6<span class="caret">▼</span></th><th>STAT 7<span class="caret">▼</span></th><th>STAT 8<span class="caret">▼</span></th><th>STAT 9<span class="caret">▼</span></th></tr></thead>
    <tbody>
      <tr><td class="fav on">★</td><td class="id">Model 1</td><td>Materials</td><td>2019/07/03<br>12:15:00.000</td><td>30.2288</td><td>2.01574</td><td>22.305</td><td class="neg">-0.149368</td><td>22.3054</td><td>4.63714</td><td>0.945706</td><td>2.81949</td><td>2.60858</td><td>1.84256</td></tr>
      <tr><td class="fav">☆</td><td class="id">Model 2</td><td>Industrials</td><td>2019/07/03<br>12:15:00.000</td><td>32.8694</td><td>0.87307</td><td>32.185</td><td class="neg">-0.0336927</td><td>33.9911</td><td>11.5693</td><td class="neg">-0.472968</td><td class="neg">-0.830458</td><td>6.80646</td><td>0.39612</td></tr>
      <tr><td class="fav">☆</td><td class="id">Model 3</td><td>Consumer<br>Discretionary</td><td>2019/07/03<br>12:15:00.000</td><td>1.66002</td><td class="neg">-0.569222</td><td>159.814</td><td>0.0252328</td><td>172.616</td><td>10.2875</td><td class="neg">-0.750396</td><td class="neg">-0.385309</td><td>4.69146</td><td>1.31029</td></tr>
      <tr><td class="fav on">★</td><td class="id">Model 4</td><td>Information<br>Technology</td><td>2019/07/03<br>12:15:00.000</td><td>45.6856</td><td>0.412148</td><td>202.488</td><td>0.00849232</td><td>205.834</td><td>11.9094</td><td class="neg">-0.137913</td><td>0.449595</td><td>3.85106</td><td>0.02858</td></tr>
      <tr><td class="fav on">★</td><td class="id">Model 5</td><td>Information<br>Technology</td><td>2019/07/03<br>12:15:00.000</td><td>75.7733</td><td>7.06728</td><td>188.605</td><td>0.016913</td><td>181.665</td><td>3.82241</td><td>0.981019</td><td>1.29847</td><td>3.34927</td><td>1.88511</td></tr>
      <tr><td class="fav">☆</td><td class="id">Model 6</td><td>Industrials</td><td>2019/07/03<br>12:15:00.000</td><td>4.96502</td><td class="neg">-0.00369</td><td>48.923</td><td>0.179453</td><td>54.19</td><td>6.02448</td><td>0.183421</td><td>0.118642</td><td>6.80646</td><td>4.00219</td></tr>
      <tr><td class="fav">☆</td><td class="id">Model 7</td><td>Industrials</td><td>2019/07/03<br>12:15:00.000</td><td>22.94521</td><td>1.00634</td><td>82.735</td><td class="neg">-0.005328</td><td>62.4901</td><td>9.25216</td><td>0.037253</td><td>0.294521</td><td>4.69146</td><td>10.82611</td></tr>
      <tr><td class="fav">☆</td><td class="id">Model 8</td><td>Information<br>Technology</td><td>2019/07/03<br>12:15:00.000</td><td>2.48091</td><td>0.92301</td><td>98.3865</td><td>0.117436</td><td>66.004</td><td>7.82366</td><td>0.286345</td><td>0.3368901</td><td>3.85106</td><td>4.01112</td></tr>
      <tr><td class="fav">☆</td><td class="id">Model 9</td><td>Information<br>Technology</td><td>2019/07/03<br>12:15:00.000</td><td>29.0965</td><td>1.99652</td><td>54.9202</td><td>0.129685</td><td>49.002</td><td>5.92456</td><td>0.62961</td><td>1.1190652</td><td>3.34927</td><td>0.91734</td></tr>
      <tr><td class="fav">☆</td><td class="id">Model 10</td><td>Materials</td><td>2019/07/03<br>12:15:00.000</td><td>10.9523</td><td>3.95261</td><td>62.816</td><td>0.62341</td><td>91.8452</td><td>8.02261</td><td>0.3889</td><td>1.008442</td><td>6.80646</td><td>5.55299</td></tr>
    </tbody>
  </table>
  <div class="pager" style="left:1299px"><span class="prev"><svg viewBox="0 0 12 12"><path d="M10 6H2m3-3L2 6l3 3"/></svg></span><span class="next"><svg viewBox="0 0 12 12"><path d="M2 6h8M7 3l3 3-3 3"/></svg></span></div>
</section>

<!-- ===== Models menu and filters ===== -->
<section class="screen screen--filters">
  <header class="topbar">
    <div class="brand">HLX</div>
    <div class="nav-item is-active" style="left:384px"><svg viewBox="0 0 16 16"><path d="M8 5a3 3 0 1 0 0 6 3 3 0 0 0 0-6zm6.5 4-.1-2 1.6-1.3-1.5-2.6-2 .7-1.7-1L10.5 1h-3l-.4 2-1.7 1-2-.8L1.9 5.8 3.5 7l-.1 2-1.6 1.2 1.5 2.6 2-.7 1.7 1 .4 2h3l.4-2 1.7-1 2 .7 1.5-2.6z"/></svg>Models</div>
    <div class="nav-item" style="left:496px"><svg viewBox="0 0 16 16"><path d="M8 1l2.2 4.6 5 .6-3.7 3.4 1 5L8 12.2 3.5 14.6l1-5L.8 6.2l5-.6z"/></svg>Favourites</div>
    <div class="nav-item" style="left:630px"><svg viewBox="0 0 16 16"><path d="M1 5h11l-3-3h2l4 4-4 4H9l3-3H1zm14 6H4l3 3H5l-4-4 4-4h2L4 9h11z"/></svg>Sensitivities</div>
    <div class="nav-item" style="left:775px"><svg viewBox="0 0 16 16"><circle cx="8" cy="4.5" r="3.5"/><path d="M1 16c0-4 3-7 7-7s7 3 7 7z"/></svg>Portfolio</div>
    <div class="nav-item" style="left:901px"><svg viewBox="0 0 16 16"><path d="M10 0 3 9h4l-2 7 8-10H9z"/></svg>Backtest</div>
    <div class="user">Username <svg viewBox="0 0 10 10"><path d="M1 3l4 4 4-4"/></svg></div>
  </header>
  <div class="page-head">
    <h1 class="page-title">MODELS</h1>
    <div class="select" style="left:190px;width:146px">Equities<svg viewBox="0 0 12 12"><path d="M1 4l5 5 5-5"/></svg></div>
    <div class="select" style="left:350px;width:96px">250D<svg viewBox="0 0 12 12"><path d="M1 4l5 5 5-5"/></svg></div>
    <div class="btn btn--export" style="left:882px"><svg viewBox="0 0 14 14" fill="none" stroke="#fff" stroke-width="1.5"><path d="M6 2H1v11h11V8M8 1h5v5M13 1 6 8"/></svg>EXPORT</div>
    <div class="btn btn--filter is-on" style="left:982px"><svg viewBox="0 0 14 14" fill="#fff"><path d="M0 1h14L9 7v6L5 11V7z"/></svg>FILTER</div>
  </div>
  <table class="models">
    <colgroup><col style="width:40px"><col style="width:90px"><col style="width:137px"><col style="width:105px"><col style="width:97px"><col style="width:97px"><col style="width:97px"><col style="width:97px"><col style="width:97px"><col style="width:97px"><col style="width:97px"><col style="width:105px"><col style="width:105px"><col style="width:105px"></colgroup>
    <thead><tr><th></th><th class="id">ID<span class="caret">▼</span></th><th>SECTOR<span class="caret">▼</span></th><th>TIME<span class="caret">▼</span></th><th>QUALITY<span class="caret">▼</span></th><th>STAT 1<span class="caret">▼</span></th><th>STAT 2<span class="caret">▼</span></th><th>STAT 3<span class="caret">▼</span></th><th>STAT 4<span class="caret">▼</span></th><th>STAT 5<span class="caret">▼</span></th><th>STAT 6<span class="caret">▼</span></th><th>STAT 7<span class="caret">▼</span></th><th>STAT 8<span class="caret">▼</span></th><th>STAT 9<span class="caret">▼</span></th></tr></thead>
    <tbody>
      <tr><td class="fav on">★</td><td class="id">Model 1</td><td>Materials</td><td>2019/07/03<br>12:15:00.000</td><td>30.2288</td><td>2.01574</td><td>22.305</td><td class="neg">-0.149368</td><td>22.3054</td><td>4.63714</td><td>0.945706</td><td>2.81949</td><td>2.60858</td><td>1.84256</td></tr>
      <tr><td class="fav">☆</td><td class="id">Model 2</td><td>Industrials</td><td>2019/07/03<br>12:15:00.000</td><td>32.8694</td><td>0.87307</td><td>32.185</td><td class="neg">-0.0336927</td><td>33.9911</td><td>11.5693</td><td class="neg">-0.472968</td><td class="neg">-0.830458</td><td>6.80646</td><td>0.39612</td></tr>
      <tr><td class="fav">☆</td><td class="id">Model 3</td><td>Consumer<br>Discretionary</td><td>2019/07/03<br>12:15:00.000</td><td>1.66002</td><td class="neg">-0.569222</td><td>159.814</td><td>0.0252328</td><td>172.616</td><td>10.2875</td><td class="neg">-0.750396</td><td class="neg">-0.385309</td><td>4.69146</td><td>1.31029</td></tr>
      <tr><td class="fav on">★</td><td class="id">Model 4</td><td>Information<br>Technology</td><td>2019/07/03<br>12:15:00.000</td><td>45.6856</td><td>0.412148</td><td>202.488</td><td>0.00849232</td><td>205.834</td><td>11.9094</td><td class="neg">-0.137913</td><td>0.449595</td><td>3.85106</td><td>0.02858</td></tr>
      <tr><td class="fav on">★</td><td class="id">Model 5</td><td>Information<br>Technology</td><td>2019/07/03<br>12:15:00.000</td><td>75.7733</td><td>7.06728</td><td>188.605</td><td>0.016913</td><td>181.665</td><td>3.82241</td><td>0.981019</td><td>1.29847</td><td>3.34927</td><td>1.88511</td></tr>
      <tr><td class="fav">☆</td><td class="id">Model 6</td><td>Industrials</td><td>2019/07/03<br>12:15:00.000</td><td>4.96502</td><td class="neg">-0.00369</td><td>48.923</td><td>0.179453</td><td>54.19</td><td>6.02448</td><td>0.183421</td><td>0.118642</td><td>6.80646</td><td>4.00219</td></tr>
      <tr><td class="fav">☆</td><td class="id">Model 7</td><td>Industrials</td><td>2019/07/03<br>12:15:00.000</td><td>22.94521</td><td>1.00634</td><td>82.735</td><td class="neg">-0.005328</td><td>62.4901</td><td>9.25216</td><td>0.037253</td><td>0.294521</td><td>4.69146</td><td>10.82611</td></tr>
      <tr><td class="fav">☆</td><td class="id">Model 8</td><td>Information<br>Technology</td><td>2019/07/03<br>12:15:00.000</td><td>2.48091</td><td>0.92301</td><td>98.3865</td><td>0.117436</td><td>66.004</td><td>7.82366</td><td>0.286345</td><td>0.3368901</td><td>3.85106</td><td>4.01112</td></tr>
      <tr><td class="fav">☆</td><td class="id">Model 9</td><td>Information<br>Technology</td><td>2019/07/03<br>12:15:00.000</td><td>29.0965</td><td>1.99652</td><td>54.9202</td><td>0.129685</td><td>49.002</td><td>5.92456</td><td>0.62961</td><td>1.1190652</td><td>3.34927</td><td>0.91734</td></tr>
      <tr><td class="fav">☆</td><td class="id">Model 10</td><td>Materials</td><td>2019/07/03<br>12:15:00.000</td><td>10.9523</td><td>3.95261</td><td>62.816</td><td>0.62341</td><td>91.8452</td><td>8.02261</td><td>0.3889</td><td>1.008442</td><td>6.80646</td><td>5.55299</td></tr>
    </tbody>
  </table>
  <div class="pager" style="left:1042px"><span class="prev"><svg viewBox="0 0 12 12"><path d="M10 6H2m3-3L2 6l3 3"/></svg></span><span class="next"><svg viewBox="0 0 12 12"><path d="M2 6h8M7 3l3 3-3 3"/></svg></span></div>
  <ul class="menu">
    <li>EQUITIES</li><li>ETFS</li><li>PAIRS</li><li>ETF PAIRS</li><li>FACTORS</li>
  </ul>
  <aside class="filters">
    <svg class="close" viewBox="0 0 14 14"><path d="M2 2l10 10M12 2 2 12"/></svg>
    <div class="scroll"></div>
    <h2>FILTERS</h2>
    <label>SECTORS</label><div class="field"><svg viewBox="0 0 12 12" fill="none" stroke="#2a5580" stroke-width="1.3"><path d="M2 4l4 4 4-4"/></svg></div>
    <label>TIME FROM</label><div class="field"><svg viewBox="0 0 12 12" fill="#2a5580"><path d="M1 3h10v8H1zm2-2h1v2H3zm5 0h1v2H8z"/></svg></div>
    <label>TIME TO</label><div class="field"><svg viewBox="0 0 12 12" fill="#2a5580"><path d="M1 3h10v8H1zm2-2h1v2H3zm5 0h1v2H8z"/></svg></div>
    <label>QUALITY</label><div class="pair"><div class="field"><span>More than</span><svg viewBox="0 0 12 12" fill="none" stroke="#2a5580" stroke-width="1.3"><path d="M2 4l4 4 4-4"/></svg></div><div class="field">1.5</div></div>
    <label>STAT 1</label><div class="pair"><div class="field"><span></span><svg viewBox="0 0 12 12" fill="none" stroke="#2a5580" stroke-width="1.3"><path d="M2 4l4 4 4-4"/></svg></div><div class="field"></div></div>
    <label>STAT 2</label><div class="pair"><div class="field"><span></span><svg viewBox="0 0 12 12" fill="none" stroke="#2a5580" stroke-width="1.3"><path d="M2 4l4 4 4-4"/></svg></div><div class="field"></div></div>
    <label>STAT 3</label><div class="pair"><div class="field"><span></span><svg viewBox="0 0 12 12" fill="none" stroke="#2a5580" stroke-width="1.3"><path d="M2 4l4 4 4-4"/></svg></div><div class="field"></div></div>
    <label>STAT 4</label><div class="pair"><div class="field"><span></span><svg viewBox="0 0 12 12" fill="none" stroke="#2a5580" stroke-width="1.3"><path d="M2 4l4 4 4-4"/></svg></div><div class="field"></div></div>
    <div class="actions"><span class="reset">RESET</span><span class="apply">APPLY</span></div>
  </aside>
</section>

</div>
</body>
</html>
```